VELMARA IMAGING
Ultrasound Imaging Services
VELMARA IMAGING - Imaging
Creative Brief
Professional
Dorvan Tessliff
Ultrasound Diagnostic
5873 Calloway ridge ln Raleigh, NC 27614
dorvantessliff@mailvane.net
Concepts
Logo for mobile ultrasound

```html
<!DOCTYPE html>
<html lang="en">
<head>
<meta charset="utf-8">
<title>Velmara Imaging – Business Card</title>
<link href="https://fonts.googleapis.com/css2?family=Exo+2:wght@400;500;800&display=swap" rel="stylesheet">
<style>
  :root{
    --bg:#e9ebee;
    --card:#ffffff;
    --navy:#272a82;
    --sky:#3fb4dd;
    --rule:#9aa0ad;
    --white:#ffffff;
  }
  *{margin:0;padding:0;box-sizing:border-box}
  html,body{width:1200px;height:901px;overflow:hidden;background:var(--bg)}
  body{font-family:"Exo 2",sans-serif}
  .business-card{
    position:absolute;left:100px;top:165px;width:1000px;height:571px;
    border-radius:44px;overflow:hidden;background:var(--card);
    box-shadow:0 14px 40px rgba(20,24,60,.18);
  }
  .card-background{position:absolute;inset:0}
  .brand{position:absolute;right:48px;top:96px;display:flex;align-items:center;gap:16px;
    font-weight:800;font-size:54px;line-height:1;color:var(--navy);letter-spacing:1.5px;white-space:nowrap}
  .brand-dot{width:26px;height:26px;border-radius:50%;background:var(--sky);flex:none}
  .holder{position:absolute;left:48px;top:352px;color:var(--white)}
  .holder-name{font-weight:500;font-size:25px;letter-spacing:1.5px}
  .holder-role{font-size:17px;margin-top:2px}
  .holder-address{font-size:17px;line-height:1.35;margin-top:24px}
  .contact-list{position:absolute;right:40px;top:385px;list-style:none;color:var(--white);font-size:17px;text-align:right}
  .contact-list li{display:flex;justify-content:flex-end;align-items:center;gap:10px;height:30px}
  .contact-list svg{width:16px;height:16px;flex:none}
</style>
</head>
<body>
  <section class="business-card">
    <svg class="card-background" viewBox="0 0 1000 571" preserveAspectRatio="none" aria-hidden="true">
      <path d="M0 250 C260 230 420 395 690 380 C820 372 920 340 1000 318 L1000 571 L0 571 Z" fill="var(--sky)"/>
      <path d="M0 262 C260 250 420 412 690 398 C820 390 920 360 1000 340 L1000 571 L0 571 Z" fill="var(--white)"/>
      <path d="M0 270 C260 260 420 420 690 406 C820 398 920 368 1000 348" fill="none" stroke="var(--rule)" stroke-width="3"/>
      <path d="M0 276 C260 268 420 428 690 414 C820 406 920 376 1000 356 L1000 571 L0 571 Z" fill="var(--navy)"/>
    </svg>

    <div class="brand"><span class="brand-dot"></span>VELMARA IMAGING</div>

    <div class="holder">
      <div class="holder-name">DORVAN TESSLIFF</div>
      <div class="holder-role">Managing Director</div>
      <div class="holder-address">5873 Calloway ridge ln<br>Raleigh, NC 27614</div>
    </div>

    <ul class="contact-list">
      <li>012 555 0148
        <svg viewBox="0 0 16 16"><path d="M3 1h3l1.5 4-2 1.3a9 9 0 0 0 4.2 4.2L11 8.5l4 1.5v3a2 2 0 0 1-2 2A12 12 0 0 1 1 3a2 2 0 0 1 2-2z" fill="currentColor"/></svg></li>
      <li>012 555 0149
        <svg viewBox="0 0 16 16"><rect x="4" y="1" width="8" height="14" rx="1.5" fill="none" stroke="currentColor" stroke-width="1.6"/><circle cx="8" cy="12.3" r="1" fill="currentColor"/></svg></li>
      <li>012 555 0150
        <svg viewBox="0 0 16 16"><rect x="4" y="1" width="8" height="5" fill="none" stroke="currentColor" stroke-width="1.4"/><rect x="1" y="6" width="14" height="6" rx="1" fill="currentColor"/><rect x="4" y="10" width="8" height="5" fill="var(--navy)" stroke="currentColor" stroke-width="1.4"/></svg></li>
      <li>dorvantessliff@mailvane.net
        <svg viewBox="0 0 16 16"><rect x="1" y="3" width="14" height="10" rx="1" fill="none" stroke="currentColor" stroke-width="1.5"/><path d="M1.5 3.5 8 9l6.5-5.5" fill="none" stroke="currentColor" stroke-width="1.5"/></svg></li>
      <li>www.velmaraimaging.net
        <svg viewBox="0 0 16 16"><circle cx="8" cy="8" r="6.5" fill="none" stroke="currentColor" stroke-width="1.4"/><ellipse cx="8" cy="8" rx="2.8" ry="6.5" fill="none" stroke="currentColor" stroke-width="1.2"/><path d="M1.5 8h13" stroke="currentColor" stroke-width="1.2"/></svg></li>
    </ul>
  </section>
</body>
</html>
```